I need a sci/tech/business focused podcast cover and logo

We need a podcast cover designed for Vantle FM, a podcast that explore the edges of human understanding and look at the technologies, trends and societal norms shaping our collective future. Here the world’s top minds share their passion projects and how advances in genomics, space travel, connected devices, artificial intelligence and other exponential tech is converging to create the future of tomorrow.

Title: Vantle (or can be Vantle FM depending on what looks better)

Subtitle: Exploring the Edges of Human Understanding

NOTE: Subtitle not necessary. If it looks great we are fine with or without a subtitle

Target Market(s)

business, technologists, scientists, startups
educated

Industry/Entity Type

Tech

Requirements
Should not have
• do not include a microphone!!

```html
<!DOCTYPE html>
<html lang="en">
<head>
<meta charset="utf-8">
<title>Vantle — Podcast Cover</title>
<link rel="stylesheet" href="https://fonts.googleapis.com/css2?family=Open+Sans:wght@400;700&display=swap">
<style>
  :root {
    --violet-mid: #55106f;
    --violet-glow: #6a1280;
    --navy: #170e4a;
    --band-blue: #2149d8;
    --cyan-edge: #33b6dc;
    --art-dark: #1546a0;
    --art-light: #2fb0dc;
    --ring-blue: #1d5fd0;
    --ring-deep: #0d2f8a;
    --disc: #05060d;
    --gold-line: #c9a860;
    --rule: #d9d6e4;
    --ink: #ffffff;
  }
  html, body {
    margin: 0;
    padding: 0;
    overflow: hidden;
    background: #ffffff;
  }
  .cover {
    position: relative;
    width: 1200px;
    height: 1200px;
    overflow: hidden;
    background:
      radial-gradient(ellipse 700px 520px at 560px 560px, var(--violet-glow) 0%, rgba(106,18,128,0) 70%),
      linear-gradient(180deg, #2a0c5c 0%, var(--violet-mid) 45%, #2a1060 78%, var(--navy) 100%);
    font-family: "Open Sans", sans-serif;
    color: var(--ink);
  }
  .cover__art {
    position: absolute;
    inset: 0;
  }
  .cover__title-row {
    position: absolute;
    left: 0;
    top: 820px;
    width: 1200px;
    height: 110px;
  }
  .cover__rule {
    position: absolute;
    top: 46px;
    height: 3px;
    background: var(--rule);
  }
  .cover__rule--left { left: 0; width: 358px; }
  .cover__rule--right { left: 820px; width: 380px; }
  .cover__title {
    position: absolute;
    left: 0;
    width: 1200px;
    top: 0;
    margin: 0;
    text-align: center;
    padding-left: 10px;
    box-sizing: border-box;
    font-weight: 700;
    font-size: 96px;
    line-height: 110px;
    letter-spacing: 2px;
    text-shadow: 0 4px 8px rgba(0,0,0,0.45);
  }
  .cover__subtitle {
    position: absolute;
    left: 88px;
    top: 926px;
    margin: 0;
    font-weight: 400;
    font-size: 45px;
    line-height: 60px;
    white-space: nowrap;
  }
  .cover__band {
    position: absolute;
    left: 0;
    top: 1045px;
    width: 1200px;
    height: 66px;
    background: var(--band-blue);
  }
  .cover__footer {
    position: absolute;
    left: 0;
    top: 1111px;
    width: 1200px;
    height: 89px;
    background: var(--navy);
  }
</style>
</head>
<body>
  <main class="cover">
    <svg class="cover__art" width="1200" height="1200" viewBox="0 0 1200 1200">
      <defs>
        <linearGradient id="artFill" x1="0" y1="1" x2="1" y2="0">
          <stop offset="0" stop-color="#123a8c"/>
          <stop offset="0.5" stop-color="var(--art-dark)"/>
          <stop offset="1" stop-color="var(--art-light)"/>
        </linearGradient>
        <radialGradient id="ringFill" cx="0.5" cy="0.5" r="0.5">
          <stop offset="0.85" stop-color="var(--ring-deep)"/>
          <stop offset="1" stop-color="var(--ring-blue)"/>
        </radialGradient>
        <radialGradient id="discFill" cx="0.5" cy="0.5" r="0.5">
          <stop offset="0" stop-color="#0a1a4a"/>
          <stop offset="1" stop-color="var(--disc)"/>
        </radialGradient>
        <radialGradient id="flare" cx="0.5" cy="0.5" r="0.5">
          <stop offset="0" stop-color="#ffffff" stop-opacity="0.9"/>
          <stop offset="1" stop-color="#ffffff" stop-opacity="0"/>
        </radialGradient>
      </defs>

      <polygon class="cover__edge" points="70,115 70,0 1200,0 1200,300 730,762"
               fill="var(--cyan-edge)"/>
      <polygon class="cover__illustration" role="img"
               aria-label="Illustration: glowing blue circuit board with binary digits and traces leading to the centre"
               points="70,0 1200,0 1200,315 730,745 70,112"
               fill="url(#artFill)"/>
      <polygon class="cover__corner" points="88,20 223,20 223,148" fill="var(--art-light)" opacity="0.85"/>

      <g class="cover__accent-lines" stroke="var(--gold-line)" stroke-width="1.5" opacity="0.7" fill="none">
        <line x1="210" y1="175" x2="740" y2="680"/>
        <line x1="1200" y1="225" x2="750" y2="675"/>
      </g>
      <g class="cover__edge-lines" stroke="var(--cyan-edge)" stroke-width="3" opacity="0.8" fill="none">
        <line x1="200" y1="200" x2="720" y2="690"/>
      </g>

      <ellipse cx="355" cy="370" rx="40" ry="6" transform="rotate(43 355 370)" fill="url(#flare)"/>
      <ellipse cx="1000" cy="480" rx="40" ry="6" transform="rotate(-43 1000 480)" fill="url(#flare)"/>

      <g class="cover__emblem">
        <circle cx="680" cy="360" r="170" fill="url(#ringFill)"/>
        <circle cx="680" cy="360" r="170" fill="none" stroke="var(--ring-blue)" stroke-width="4"/>
        <circle cx="680" cy="360" r="150" fill="url(#discFill)" role="img"
                aria-label="Illustration: blue line drawing of a human head in profile showing the brain"/>
        <circle cx="680" cy="360" r="150" fill="none" stroke="var(--ring-blue)" stroke-width="3"/>
      </g>
    </svg>

    <div class="cover__title-row">
      <span class="cover__rule cover__rule--left"></span>
      <h1 class="cover__title">VANTLE</h1>
      <span class="cover__rule cover__rule--right"></span>
    </div>
    <p class="cover__subtitle">Exploring the Edges of Human Understanding</p>

    <div class="cover__band"></div>
    <div class="cover__footer"></div>
  </main>
</body>
</html>
```